Corvane Project Services - Flyer

Project Breif:
I need a single page A4 Capability Statement, which will be used to market our services to prospective clients, both in print and via email PDF.
It needs to look professional and should incorporate the elements I have uploaded into files, these include:
Capability Statement Text
Corvane Services Company Logo
Additional Logo’s (Tools We Use)
Glimmer Bay Pics can be cut into the page
I have included examples of capability statements as a guide to what i am looking for.
Regards
Derek
Engineering Consulting

```html
<!DOCTYPE html>
<html lang="en">
<head>
<meta charset="utf-8">
<title>Corvane Project Services – Capability Statement</title>
<link href="https://fonts.googleapis.com/css2?family=Roboto:wght@300;400;700&display=swap" rel="stylesheet">
<style>
  :root{
    --brand-blue:#4a89c8;
    --heading-blue:#4f8cca;
    --ink:#1d1d1d;
    --body-grey:#555a60;
    --tab-dark:#333335;
    --paper:#ffffff;
    --backdrop:#d4d5d7;
  }
  *{box-sizing:border-box;margin:0;padding:0}
  html,body{width:1200px;height:1200px;overflow:hidden;background:var(--backdrop);font-family:"Roboto",Arial,sans-serif}
  .flyer{position:absolute;left:175px;top:51px;width:817px;height:1056px;background:var(--paper);
    transform:scale(1.04);transform-origin:top left;box-shadow:0 4px 14px rgba(0,0,0,.25);overflow:hidden}
  .flyer-shapes{position:absolute;inset:0}
  .abs{position:absolute}
  .title{left:387px;top:26px;color:#fff;font-weight:700;font-size:31px;letter-spacing:.3px}
  .brand{left:34px;top:60px;width:250px;text-align:center;color:var(--brand-blue)}
  .brand-mark{width:44px;height:44px;border-radius:50%;background:var(--brand-blue);margin:0 auto 12px}
  .brand-name{font-size:17px;font-weight:700;letter-spacing:1.5px;line-height:1.2}
  .intro{left:52px;top:366px;width:292px}
  .intro h1{font-weight:300;font-size:23.5px;line-height:28px;color:var(--heading-blue);margin-bottom:20px}
  .intro p{font-size:16px;line-height:19.3px;color:var(--body-grey);margin-bottom:18px;font-weight:400}
  .services{left:417px;top:363px;width:358px}
  .services h2{font-weight:300;font-size:28px;color:var(--heading-blue);margin-bottom:20px}
  .service{position:relative;padding-left:49px;margin-bottom:17px}
  .service svg{position:absolute;left:0;top:-6px}
  .service h3{font-size:15.5px;font-weight:700;color:var(--ink);line-height:19px}
  .service ul{list-style:none}
  .service li{position:relative;padding-left:27px;font-size:16px;line-height:19.2px;color:var(--body-grey)}
  .service li::before{content:"";position:absolute;left:6px;top:7px;width:6px;height:6px;border-radius:50%;background:var(--brand-blue)}
  .contact-tab{left:386px;top:922px;width:167px;height:35px;background:var(--tab-dark);color:#fff;font-size:21px;text-align:center;line-height:35px}
  .contact-list{left:507px;top:963px;list-style:none}
  .contact-list li{display:flex;align-items:center;gap:10px;color:#fff;font-size:14.5px;height:20px}
  .contact-list svg{width:16px;height:14px;flex:none}
  .tools{left:28px;top:960px;width:360px}
  .tool-row{display:flex;align-items:center;gap:16px;height:40px}
  .tool{display:flex;align-items:center;gap:5px;font-size:14px;font-weight:700;color:var(--body-grey);white-space:nowrap}
  .tool i{display:inline-block;width:14px;height:14px;background:var(--brand-blue)}
  .tool i.round{border-radius:50%}
</style>
</head>
<body>
<article class="flyer">
  <svg class="flyer-shapes" width="817" height="1056" viewBox="0 0 817 1056">
    <defs>
      <linearGradient id="meetingTones" x1="0" y1="0" x2="1" y2="1">
        <stop offset="0" stop-color="#c9d6e6"/>
        <stop offset=".45" stop-color="#eef3f8"/>
        <stop offset="1" stop-color="#b7c9de"/>
      </linearGradient>
      <linearGradient id="chartTones" x1="0" y1="0" x2="1" y2="0">
        <stop offset="0" stop-color="#dfe6ee"/>
        <stop offset="1" stop-color="#f3f5f8"/>
      </linearGradient>
    </defs>
    <rect role="img" aria-label="Photo: colleagues reviewing documents at a desk" x="0" y="80" width="817" height="256" fill="url(#meetingTones)"/>
    <polygon points="0,0 360,0 288,182 0,182" fill="#fff"/>
    <polygon points="360,0 817,0 817,80 330,80" fill="var(--brand-blue)"/>
    <rect role="img" aria-label="Photo: printed Gantt chart with a pen" x="0" y="848" width="390" height="102" fill="url(#chartTones)"/>
    <polygon points="387,957 414,957 440,990" fill="#b9bbbe"/>
    <polygon points="553,929 817,929 817,1056 452,1056 414,957 553,957" fill="var(--brand-blue)"/>
  </svg>

  <div class="abs title">CAPABILITY STATEMENT</div>
  <div class="abs brand">
    <div class="brand-mark"></div>
    <div class="brand-name">CORVANE PROJECT<br>SERVICES</div>
  </div>

  <section class="abs intro">
    <h1>Corvane Project Services Ltd. is a leading project control consultancy based in Co Cork Ireland</h1>
    <p>For over 20 years we have been helping our clients to deliver complex projects and programs throughout main-land Europe.</p>
    <p>We are passionate about empower organisations to achieve their objectives, on time and on budget.</p>
    <p>We are continually innovating, evolving and learning, utilize the latest industry tools and techniques to deliver real value to our clients.</p>
    <p>Our goal is to make successful project delivery more achievable and repeatable.</p>
  </section>

  <section class="abs services">
    <h2>Core Services:</h2>
    <div class="service">
      <svg width="32" height="30" viewBox="0 0 32 30" fill="none" stroke="var(--brand-blue)" stroke-width="1.3"><rect x="2" y="4" width="26" height="22" rx="1"/><line x1="2" y1="10" x2="28" y2="10"/><line x1="8" y1="1" x2="8" y2="6"/><line x1="22" y1="1" x2="22" y2="6"/><path d="M7 14h2M12 14h2M17 14h2M22 14h2M7 18h2M12 18h2M17 18h2M22 18h2M7 22h2M12 22h2"/></svg>
      <h3>Planning and Scheduling</h3>
      <ul><li>Tender Planning</li><li>Interactive Planning / Pull Planning</li><li>EPCMV Planning &amp; Scheduling</li><li>Schedule Earned Value Management</li><li>Independent Schedule Quality Assessment</li><li>Schedule Risk Analysis (Monte Carlo) Training</li></ul>
    </div>
    <div class="service">
      <svg width="32" height="32" viewBox="0 0 32 32" fill="none" stroke="var(--brand-blue)" stroke-width="1.3"><rect x="3" y="2" width="20" height="27" rx="1"/><path d="M7 8h12M7 12h12M7 16h10M7 20h8"/><circle cx="24" cy="23" r="5"/><path d="M24 20v3.5M24 25.5v.5"/></svg>
      <h3>Management of Risk</h3>
      <ul><li>Risk Management Policies &amp; Procedures</li><li>Risk Management Strategy</li><li>Risk Registers</li><li>Risk Improvement Planning</li><li>Risk Response and Communication</li><li>Risk Management Training</li></ul>
    </div>
    <div class="service">
      <svg width="32" height="32" viewBox="0 0 32 32" fill="none" stroke="var(--brand-blue)" stroke-width="1.3"><path d="M9 4h8l-2 5h-4z"/><path d="M11 9c-6 4-8 9-6 14 1 3 5 4 8 4h3"/><path d="M15 9c3 2 5 4 6 7"/><rect x="17" y="16" width="12" height="13" rx="1"/><path d="M20 20h6M20 23h6M20 26h6"/><path d="M11 14v9M9 16h3.5a1.5 1.5 0 010 3H9.5a1.5 1.5 0 000 3H13"/></svg>
      <h3>Cost Control:</h3>
      <ul><li>Estimating &amp; Forecasting</li><li>Earned Value Analysis</li><li>Progress Reporting</li><li>Cost Risk Analysis</li></ul>
    </div>
  </section>

  <div class="abs tools">
    <div class="tool-row">
      <span class="tool"><i></i>Tessaro Plan</span>
      <span class="tool"><i></i>Plotwise</span>
      <span class="tool"><i></i>Rindle Planner</span>
    </div>
    <div class="tool-row">
      <span class="tool">Markstone Pro</span>
      <span class="tool">Veltra Audit</span>
      <span class="tool"><i class="round"></i>Rivora</span>
    </div>
  </div>

  <div class="abs contact-tab">Contact Us</div>
  <ul class="abs contact-list">
    <li><svg viewBox="0 0 16 14" fill="#fff"><circle cx="8" cy="4" r="3.3"/><path d="M1.5 14c0-4 3-6 6.5-6s6.5 2 6.5 6z"/></svg>Derek Halloran (Managing Director)</li>
    <li><svg viewBox="0 0 16 14" fill="none" stroke="#fff" stroke-width="2.2" stroke-linecap="round"><path d="M5 2C2 5 2 9 5 12"/><path d="M5 2h3M5 12h3"/></svg>+353 (0)870 555 014</li>
    <li><svg viewBox="0 0 16 14" fill="none" stroke="#fff" stroke-width="1.3"><rect x="2" y="3" width="12" height="8"/><path d="M2 3l6 5 6-5M2 11l4.5-4M14 11l-4.5-4"/></svg>info@corvaneservices.ie</li>
    <li><svg viewBox="0 0 16 14" fill="none" stroke="#fff" stroke-width="1.2"><circle cx="8" cy="7" r="6"/><ellipse cx="8" cy="7" rx="2.6" ry="6"/><path d="M2 7h12M3 4h10M3 10h10"/></svg>www.corvaneservices.ie</li>
  </ul>
</article>
</body>
</html>
```